Elementary School Profile of a Falconet

Please recreate a poster of our Profile of a Falconet traits that we desire to have when they graduate from 4th grade. This should be kid-friendly and kid-themed with icons to help communicate the Competencies. See attached six competencies and the "I can" statements next to. Our colors are navy, red and white. Our logo is attached as well. This will be made into a poster and displayed in each classroom, the office, and also used on social media.

```html
<!DOCTYPE html>
<html lang="en">
<head>
<meta charset="utf-8">
<title>Profile of a Falconet – Early Learners &amp; Elementary School</title>
<link href="https://fonts.googleapis.com/css2?family=Luckiest+Guy&family=Poppins:wght@700&family=Rubik:wght@500;600&family=Barlow:wght@400;600&display=swap" rel="stylesheet">
<style>
  :root{
    --navy:#0b1445;
    --red:#8e0d1c;
    --white:#ffffff;
    --sky-top:#9fd2ef;
    --sky-mid:#c4e6f7;
    --sky-low:#a9dcf3;
    --card:#ebe9ea;
    --card-line:#c9c7c9;
    --card-border:#8f8f96;
    --ink:#1b1b24;
    --grass-top:#7cc35a;
    --grass-low:#3f9a2e;
  }
  *{box-sizing:border-box;margin:0;padding:0}
  html,body{width:905px;height:1200px;overflow:hidden;background:var(--sky-mid)}
  .poster{
    position:relative;width:905px;height:1200px;overflow:hidden;
    background:linear-gradient(180deg,var(--sky-top) 0%,var(--sky-mid) 40%,var(--sky-low) 70%,#c8ecf6 100%);
    font-family:"Barlow",sans-serif;color:var(--ink);
  }
  .meadow{
    position:absolute;left:0;right:0;bottom:0;height:330px;
    background:linear-gradient(180deg,var(--grass-top) 0%,#63b344 35%,var(--grass-low) 100%);
    border-radius:60% 40% 0 0 / 60px 40px 0 0;
  }
  .crest{
    position:absolute;left:50px;top:72px;display:flex;align-items:center;gap:10px;
  }
  .crest-dot{width:38px;height:38px;border-radius:50%;background:var(--navy)}
  .crest-name{font-family:"Luckiest Guy",sans-serif;font-size:34px;color:var(--red);line-height:1}
  .title{
    position:absolute;left:290px;top:44px;width:420px;
    font-family:"Luckiest Guy",sans-serif;color:var(--red);
    font-size:58px;line-height:1.05;letter-spacing:1px;
  }
  .badge{
    position:absolute;left:722px;top:40px;width:124px;height:124px;border-radius:50%;
    background:var(--navy);color:var(--white);display:flex;align-items:center;justify-content:center;
    text-align:center;font-family:"Luckiest Guy",sans-serif;font-size:17px;line-height:1.15;padding-top:4px;
  }
  .subtitle{
    position:absolute;left:0;right:0;top:184px;text-align:center;
    font-family:"Rubik",sans-serif;font-weight:600;font-size:25px;line-height:1.15;
  }
  .subtitle .district{color:var(--navy);display:block}
  .subtitle .school{color:var(--red);display:block}
  .traits{
    position:absolute;left:56px;top:262px;width:790px;
    display:grid;grid-template-columns:383px 383px;column-gap:24px;row-gap:50px;
  }
  .trait-head{display:flex;align-items:center;gap:12px;height:36px;margin-bottom:6px}
  .trait-icon{width:26px;height:26px;border-radius:6px;flex:none}
  .icon-warm{background:linear-gradient(135deg,#f2b66b,#e56d5b)}
  .icon-cool{background:linear-gradient(135deg,#7ec8f2,#f4c44a)}
  .icon-mix{background:linear-gradient(135deg,#f29a4a,#5aa8e8)}
  .trait-name{font-family:"Poppins",sans-serif;font-weight:700;font-size:30px;color:var(--navy);line-height:1}
  .trait-card{
    list-style:none;height:222px;background:var(--card);border:1px solid var(--card-border);
    border-radius:12px;display:flex;flex-direction:column;overflow:hidden;
  }
  .trait-card li{
    flex:1;display:flex;align-items:center;padding:4px 12px 4px 38px;position:relative;
    font-size:17.5px;line-height:1.2;border-top:1px solid var(--card-line);
  }
  .trait-card li:first-child{border-top:none}
  .trait-card li::before{
    content:"";position:absolute;left:19px;top:50%;width:10px;height:10px;margin-top:-5px;
    border-radius:50%;background:var(--red);
  }
  .trait-card li::after{
    content:"";position:absolute;left:22px;top:50%;width:3px;height:5px;margin-top:-4px;
    border:solid var(--white);border-width:0 1.5px 1.5px 0;transform:rotate(45deg);
  }
  .trait-card li p{position:relative;top:-1px}
  .lead{font-weight:600;color:var(--red)}
  .lead-dark{font-weight:600;color:var(--ink)}
</style>
</head>
<body>
<main class="poster">
  <div class="meadow" role="img" aria-label="Green grass meadow with colorful eggs and daisies"></div>

  <div class="crest"><span class="crest-dot"></span><span class="crest-name">Falconets</span></div>

  <h1 class="title">Profile of a Falconet</h1>

  <div class="badge">Early<br>Learners &amp;<br>Elementary<br>School</div>

  <h2 class="subtitle">
    <span class="district">Cedar Hollow Public Schools:</span>
    <span class="school">Profile of a Falconet Early Learners and Elementary School</span>
  </h2>

  <section class="traits">
    <article class="trait">
      <div class="trait-head"><span class="trait-icon icon-warm" role="img" aria-label="Communicator icon"></span><h3 class="trait-name">Communicator</h3></div>
      <ul class="trait-card">
        <li><p><span class="lead">I can</span> use words, writing,&amp; pictures to clearly share ideas.</p></li>
        <li><p><span class="lead-dark">I can</span> look at the speaker and listen carefully to understand what they are saying.</p></li>
        <li><p><span class="lead-dark">I know</span> how to adjust my communication for different places &amp; people.</p></li>
      </ul>
    </article>

    <article class="trait">
      <div class="trait-head"><span class="trait-icon icon-cool" role="img" aria-label="Critical thinker icon"></span><h3 class="trait-name">Critical Thinker</h3></div>
      <ul class="trait-card">
        <li><p><span class="lead">I can</span> ask questions like "why" and "how" to learn more about the world.</p></li>
        <li><p><span class="lead">When</span> faced with a problem, I can be creative and come up with different solutions.</p></li>
        <li><p><span class="lead">I can</span> use facts and clues to help make wise decisions.</p></li>
      </ul>
    </article>

    <article class="trait">
      <div class="trait-head"><span class="trait-icon icon-mix" role="img" aria-label="Responsible icon"></span><h3 class="trait-name">Responsible</h3></div>
      <ul class="trait-card">
        <li><p><span class="lead">I can</span> take ownership of my actions and remember to complete my job.</p></li>
        <li><p><span class="lead">I can</span> take care of my belongings and always try my best in schoolwork.</p></li>
        <li><p><span class="lead">I can</span> tell the truth and act with integrity even when no one is watching.</p></li>
      </ul>
    </article>

    <article class="trait">
      <div class="trait-head"><span class="trait-icon icon-warm" role="img" aria-label="Adaptable icon"></span><h3 class="trait-name">Adaptable</h3></div>
      <ul class="trait-card">
        <li><p><span class="lead">When</span> a plan changes or a task is hard, I can stay calm &amp; try a new way.</p></li>
        <li><p><span class="lead">I can</span> learn from mistakes and use past knowledge to try new things.</p></li>
        <li><p><span class="lead">I can</span> work and play well with people who are different from me.</p></li>
      </ul>
    </article>

    <article class="trait">
      <div class="trait-head"><span class="trait-icon icon-cool" role="img" aria-label="Collaborator icon"></span><h3 class="trait-name">Collaborator</h3></div>
      <ul class="trait-card">
        <li><p><span class="lead">I can</span> share ideas and work together with a group to reach a common goal.</p></li>
        <li><p><span class="lead">I can</span> listen to my teammates and respect their different ideas.</p></li>
        <li><p><span class="lead">I can</span> know when to share, when to help others, and when to be the leader.</p></li>
      </ul>
    </article>

    <article class="trait">
      <div class="trait-head"><span class="trait-icon icon-mix" role="img" aria-label="Communicator icon"></span><h3 class="trait-name">Communicator</h3></div>
      <ul class="trait-card">
        <li><p><span class="lead">I can</span> be empathetic, noticing how others are feeling (happy, sad, frustrated).</p></li>
        <li><p><span class="lead">I can</span> use kind words and gentle actions to support their friends.</p></li>
        <li><p><span class="lead">I can</span> look for ways to help their school &amp; the community.</p></li>
      </ul>
    </article>
  </section>
</main>
</body>
</html>
```